Tumbleweed Backpackers DL Flyer Design

We require a two sided Flyer design to help promote Tumbleweed's Backpackers / Hostel accommodation.Give it a warm, summer vibe  to reflect Perth's great weather and the friendly hospitality that Tumbleweed's provides. Please use the attached pictures, logo and text. Our colour scheme is usually pastel blues but some warm accent colours could work too.
General advice:
The front should be exciting with pictures (or photos) that draw people in, with our contact info at the bottom.
The back should contain our bullet points, the location map with Tumbleweed address and photos.
It needs to appeal to 18 - 29 yr olds as this is our target market.
Size: 100 x 210 mm
Address: 87 Marrowvale Rd, East Perth, Western Australia, 6000, Australia
Website: http://www.tumbleweedbackpackers.com.au/
Email: reservations@tumbleweedbackpackers.com.au
Ph: +61 8 9471 3062

Target Market(s)
18 - 29
Industry/Entity Type
Accommodation

```html
<!DOCTYPE html>
<html lang="en">
<head>
<meta charset="utf-8">
<title>Tumbleweed Backpackers – DL Flyer (Back)</title>
<link rel="stylesheet" href="https://fonts.googleapis.com/css2?family=Fira+Sans:wght@400;500&family=Roboto+Condensed:wght@400;500&display=swap">
<style>
  :root {
    --backdrop: #141414;
    --panel-brown: #4f2320;
    --paper: #ffffff;
    --ink: #1e1e1e;
    --yellow: #f3e36b;
    --pale-yellow: #f1e6a0;
    --green: #c9e3a4;
    --sky: #8fcfef;
    --orange: #f5b73b;
    --pink: #f4a1a0;
    --white: #ffffff;
    --rule-blue: #4a9bd4;
    --rule-grey: #5f7483;
    --rule-tan: #9c7a70;
    --map-light: #ebe7de;
    --map-dark: #e0dbd0;
  }
  * { margin: 0; padding: 0; box-sizing: border-box; }
  html, body {
    width: 760px; height: 1200px; overflow: hidden;
    background: var(--backdrop);
  }
  .flyer {
    position: absolute; left: 142px; top: 100px;
    width: 476px; height: 1000px;
    background: var(--paper);
    font-family: "Fira Sans", sans-serif;
  }
  .hero-photo {
    position: absolute; left: 0; top: 0; width: 476px; height: 118px;
    background: linear-gradient(90deg, #6d6a66 0%, #8a4a36 30%, #7a3a2c 55%, #2a3a6e 78%, #6a6a72 100%);
  }
  .features {
    position: absolute; left: 0; top: 120px; width: 476px; height: 454px;
    background: var(--panel-brown);
  }
  .feature {
    position: absolute; white-space: nowrap; line-height: 1;
  }
  .divider {
    position: absolute; left: 0; top: 574px; width: 476px; height: 4px;
    background: linear-gradient(90deg, var(--rule-grey) 0 50%, var(--rule-tan) 50% 100%);
  }
  .contact-bar {
    position: absolute; left: 0; top: 578px; width: 476px; height: 80px;
    border-bottom: 2px solid var(--rule-blue);
  }
  .brand-mark {
    position: absolute; left: 18px; top: 14px; width: 52px; height: 52px;
    border-radius: 50%; background: #d9d9d9;
  }
  .brand-name {
    position: absolute; left: 82px; top: 10px;
    font-family: "Roboto Condensed", sans-serif; font-weight: 500;
    font-size: 19px; line-height: 19px; color: var(--ink);
  }
  .brand-url {
    position: absolute; left: 82px; top: 51px;
    font-family: "Roboto Condensed", sans-serif; font-weight: 500;
    font-size: 8px; color: var(--ink); letter-spacing: 0.3px;
  }
  .address {
    position: absolute; left: 217px; top: 20px;
    font-family: "Roboto Condensed", sans-serif; font-size: 13.5px;
    line-height: 16px; color: var(--ink); white-space: nowrap;
  }
  .address .phone { font-weight: 500; }
  .location-map {
    position: absolute; left: 13px; top: 662px; width: 447px; height: 320px;
    background: linear-gradient(160deg, var(--map-light), var(--map-dark));
  }
</style>
</head>
<body>
<main class="flyer">
  <div class="hero-photo" role="img" aria-label="Photo of the hostel common lounge with brick walls, sofas and guests at tables"></div>

  <section class="features">
    <span class="feature" style="left:59px;top:16px;font-size:27px;color:var(--yellow);font-weight:500">Award Winning</span>
    <span class="feature" style="left:275px;top:21px;font-size:19px;color:var(--green)">Central Location</span>
    <span class="feature" style="left:59px;top:49px;font-size:25px;color:var(--white)">Private lockers for every person</span>
    <span class="feature" style="left:59px;top:85px;font-size:20px;color:var(--sky)">Ensuite Dorm rooms</span>
    <span class="feature" style="left:263px;top:90px;font-size:12px;color:var(--pale-yellow)">FREE BREAKFAST AND LINEN</span>
    <span class="feature" style="left:62px;top:110px;font-size:27.4px;color:var(--white)">Female only dorms available</span>
    <span class="feature" style="left:59px;top:148px;font-size:21.3px;color:var(--orange)">Excellent kitchen and dining facilities</span>
    <span class="feature" style="left:60px;top:183px;font-size:19px;color:var(--green)">Laundry facilities on site</span>
    <span class="feature" style="left:295px;top:173px;font-size:32px;color:var(--white);font-weight:500">Free wifi</span>
    <span class="feature" style="left:59px;top:211px;font-size:23.5px;color:var(--pink)">Huge games, Movies and TV areas.</span>
    <span class="feature" style="left:60px;top:247px;font-size:13.4px;color:var(--yellow)">BASKET BALL, TABLE TENNIS, POOL TABLE AND MUCH MORE!</span>
    <span class="feature" style="left:59px;top:271px;font-size:20.3px;color:var(--white)">Food and drinks available, licensed bar</span>
    <span class="feature" style="left:61px;top:296px;font-size:28px;color:var(--yellow);font-weight:500">Free Computer use</span>
    <span class="feature" style="left:95px;top:331px;font-size:19px;color:var(--sky)">Free bus and easy access to transport</span>
    <span class="feature" style="left:58px;top:355px;font-size:23.3px;color:var(--green)">Close to local and interstate trains</span>
    <span class="feature" style="left:58px;top:385px;font-size:15px;color:var(--yellow)">WALKING DISTANCE TO NIGHTLIFE AREAS</span>
    <span class="feature" style="left:59px;top:407px;font-size:26px;color:var(--white)">24hr reception</span>
    <span class="feature" style="left:249px;top:413px;font-size:18.5px;color:var(--orange)">Safe secure parking</span>
  </section>

  <div class="divider"></div>

  <section class="contact-bar">
    <div class="brand-mark"></div>
    <div class="brand-name">Tumbleweed's<br>Backpackers</div>
    <div class="brand-url">tumbleweedbackpackers.com.au</div>
    <div class="address">
      87 Marrowvale Rd, East Perth, WA 6000<br>
      reservations@tumbleweedbackpackers.com.au<br>
      Call us : <span class="phone">+61 8 9471 3062</span>
    </div>
  </section>

  <div class="location-map" role="img" aria-label="Street map of East Perth marking the hostel location near the stadium, the freeway and East Perth station"></div>
</main>
</body>
</html>
```